A website for a green bio-plastics manufacturing company

We need a home page designed and two complimentary template pages that can be used for the rest of the website. The template page should vary in design from the home page, but should flow uniformly with it.

This is a very innovative company with a proprietary manufacturing method of using bird feathers to make plastic.

The site should be functional, informative, user-friendly and informative to both our business partners and the consumers.
Updates

I've added a more concise overview of the company.  If any of the designers have any questions for me, please ask.  Thanks

Marco

Target Market(s)

Business partners interested in using bio-plastics for their products and general customers.

Industry/Entity Type

Manufacturing

Number of Pages Required

3 pages

Requirements
Must have
• I attached some information about the company, so the site should be designed to incorporate that content.

Will need to be edited by Adobe Contribute.

Easy to navigate

One of the template pages should have one column for content. The other should have two columns. I''m open to different ideas though.

Should be very pleasing to the eye and uncluttered.

Want to be informative to both our business partners as well as consumers who may be researching our product(s)

Easy to Maintain

Anticipated Tabs/Pages
· Home Page
o General “welcome” page

· About Us
o Company overview and information

· Products
o Horticulture Containers
o Agriculture Films
o Where to Buy
o Upcoming Products

· Business Partners

· Press Releases

· Contact Us

Nice to have
• Would like to have earth tones and or nice greens in the color scheme. They make use of bird feathers for their manufacturing process, so perhaps a real sharp image of a feather can be incorporated into the design. Be creative though.

Perhaps a jQuery nav bar, but that may be out of scope.

Should not have
• No flash at all.

```html
<!DOCTYPE html>
<html lang="en">
<head>
<meta charset="utf-8">
<title>Northfield BioResins – Home and Template Pages</title>
<link href="https://fonts.googleapis.com/css2?family=Jockey+One&family=Ubuntu:wght@500;700&family=Open+Sans:wght@400;600;700&display=swap" rel="stylesheet">
<style>
:root{
  --green-dark:#0e7438;
  --green-head:#157a3c;
  --green-pale:#d8eab5;
  --green-strip:#b6d77a;
  --frame:#a9b8a4;
  --text:#6a6a6a;
  --text-dark:#333;
  --white:#fff;
}
*{box-sizing:border-box;margin:0;padding:0}
html,body{width:1200px;height:4684px;overflow:hidden;background:var(--white)}
body{position:relative;font-family:"Open Sans",sans-serif;color:var(--text);font-size:12.5px;line-height:19px;letter-spacing:.45px}
.abs{position:absolute}
.page-label{position:absolute;left:0;width:1200px;text-align:center;font-family:"Jockey One",sans-serif;font-size:42px;color:var(--green-dark);letter-spacing:1px;line-height:44px}
.nav{position:absolute;display:flex;font-weight:700;font-size:14px;color:#222;white-space:nowrap;line-height:22px;letter-spacing:0}
.nav span.sep{margin:0 10px;color:#444;font-weight:400}
.nav .active{background:var(--green-head);color:var(--white);padding:0 5px;border:1px solid #7aa}
.banner-home{left:44px;top:200px;width:1114px;height:345px;border-radius:12px;background:linear-gradient(160deg,#8cc646 0%,#6fae33 55%,#5c9a25 100%);box-shadow:0 4px 6px rgba(0,0,0,.25)}
.brand-home{position:absolute;left:26px;top:210px;font-family:"Ubuntu",sans-serif;font-weight:700;color:var(--white);font-size:50px;letter-spacing:8px;line-height:56px}
.brand-home small{display:block;font-size:30px;letter-spacing:8px;margin-left:18px}
.brand-dot{position:absolute;left:94px;top:50px;width:130px;height:130px;border-radius:50%;background:#2e8a34}
.tagline{position:absolute;background:var(--green-pale);font-family:"Ubuntu",sans-serif;font-weight:500;color:var(--green-dark);white-space:nowrap;letter-spacing:0}
.art{position:absolute;background:linear-gradient(180deg,rgba(60,154,44,.55),rgba(31,110,30,.55))}
.welcome h1{font-family:"Ubuntu",sans-serif;font-weight:700;color:var(--green-dark);font-size:34px;line-height:40px;letter-spacing:0}
.welcome p{margin-top:18px}
.divider{position:absolute;border-left:2px dotted #ccc}
.box{position:absolute;border:3px solid var(--frame);border-top:0;border-radius:10px;background:var(--white);box-shadow:1px 2px 2px rgba(0,0,0,.15)}
.box-head{height:40px;margin:0 -3px;background:var(--green-head);border-radius:9px 9px 0 0;color:var(--white);font-family:"Ubuntu",sans-serif;font-weight:500;font-size:21px;line-height:44px;padding-left:16px;letter-spacing:0}
.box-body{padding:16px 14px;color:var(--text-dark);font-size:12.5px;line-height:16px;letter-spacing:.2px}
.box-body b{font-weight:700;letter-spacing:.5px;font-size:12px}
.more-btn{position:absolute;right:18px;bottom:14px;background:var(--green-head);color:var(--white);font-weight:700;font-size:13px;padding:0 16px;border-radius:6px;line-height:20px}
.thumb{position:absolute;border:2px solid #ddd}
.ph-grey{background:linear-gradient(135deg,#f4f4f4,#9a9a9a 60%,#e6e6e6)}
.ph-green{background:linear-gradient(180deg,#cfd8cf 0%,#6b7a68 45%,#8a5a3a 80%,#4f6a3a 100%)}
.ph-film{background:linear-gradient(180deg,#4c7ecb 0%,#8fb1e0 18%,#e6e6e6 30%,#bdbdbd 65%,#f2f2f2 100%)}
.footer{position:absolute;color:#222;font-size:11px;line-height:14px;letter-spacing:.3px}
.banner-inner{left:0;width:1200px;height:138px;background:linear-gradient(180deg,#7dbb3d,#5f9e27)}
.brand-inner{position:absolute;left:44px;font-family:"Ubuntu",sans-serif;font-weight:500;color:var(--white);font-size:38px;line-height:40px;letter-spacing:0}
.brand-inner .code{font-size:24px;font-weight:700;margin-right:18px}
.crumb{position:absolute;left:0;width:1200px;height:25px;background:var(--green-strip);color:var(--green-dark);font-weight:700;font-size:13px;line-height:25px;padding-left:46px}
.col-title{font-family:"Ubuntu",sans-serif;font-weight:700;color:var(--green-dark);font-size:36px;line-height:40px;letter-spacing:0}
.txt{position:absolute;color:var(--text)}
.txt b{color:#555;font-weight:700}
.list{list-style:none;margin-top:10px}
.list li{position:relative;padding-left:22px;line-height:21.5px;color:var(--text)}
.list li::before{content:"";position:absolute;left:2px;top:6px;border-left:7px solid #222;border-top:5px solid transparent;border-bottom:5px solid transparent}
.num{position:absolute;bottom:24px;width:100%;text-align:center;color:#333;font-size:14px}
.cat-item{position:relative;height:107px}
.cat-item .ph{position:absolute;right:0;top:0;width:89px;height:80px;border:2px solid #ddd}
.cat-item b{color:#555}
.bullets p{margin-bottom:19px}
</style>
</head>
<body>

<!-- ===== HOME PAGE ===== -->
<div class="page-label" style="top:82px">HOME PAGE</div>
<nav class="nav" style="left:528px;top:173px">
  <span class="active">Home</span><span class="sep">|</span><span>Product Catalogue</span><span class="sep">|</span><span>Business Partners</span><span class="sep">|</span><span>Press Releases</span><span class="sep">|</span><span>Contact Us</span>
</nav>
<header class="abs banner-home">
  <div class="brand-dot"></div>
  <div class="brand-home">NORTHFIELD<small>BIO RESINS</small></div>
  <div class="art" role="img" aria-label="Green feather illustration" style="left:780px;top:36px;width:140px;height:200px"></div>
  <div class="tagline" style="left:556px;top:224px;width:518px;height:80px;font-size:36px;line-height:80px;text-align:center">Customers are "Partners"</div>
</header>

<section class="abs welcome" style="left:47px;top:560px;width:615px">
  <h1>Welcome!</h1>
  <p style="margin-top:10px">Northfield BioResins is a green-technology start-up company that has implemented cutting edge technology and custom-designed machines to manufacture bioplastics from poultry feathers on an industrial scale. Marco Hallworth, who brings a wealth of experience in agriculture, poultry, and business, is the entrepreneur behind the company's creation and development.</p>
  <p>Northfield BioResins plans to manufacture virgin keratin-based resins and both sell these resins and further compound them to meet desired specifications. We plan to sell manufactured and compounded resins to our business partners who will further process these resins into end user products such as: greenhouse/nursery containers, agricultural films, automotive components, and/or office furniture.</p>
</section>

<div class="box" style="left:44px;top:835px;width:703px;height:245px">
  <div class="box-head">Our Products</div>
  <div class="thumb ph-grey" role="img" aria-label="Nursery container product photo" style="left:71px;top:60px;width:134px;height:134px"></div>
  <div class="thumb ph-green" role="img" aria-label="Greenhouse product photo" style="left:286px;top:60px;width:134px;height:134px"></div>
  <div class="thumb ph-film" role="img" aria-label="Agricultural film in a field photo" style="left:500px;top:60px;width:134px;height:134px"></div>
  <div class="more-btn">More...</div>
</div>

<div class="divider" style="left:800px;top:578px;height:515px"></div>

<div class="box" style="left:855px;top:564px;width:296px;height:245px">
  <div class="box-head">Press Release</div>
  <div class="box-body" style="padding-top:12px">
    <p>Lorem Ipsum is simply dummy text of the printing and type setting industry. Lorem Ipsum has been the industry's standard dummy text ever since the 1500s.</p>
    <p style="margin-top:14px">Lorem Ipsum is simply dummy text of the printing and type setting industry.</p>
    <p style="text-align:right;margin-top:4px">More...</p>
  </div>
</div>

<div class="box" style="left:855px;top:835px;width:296px;height:245px">
  <div class="box-head">Contact Us</div>
  <div class="box-body" style="padding-top:14px">
    <p><b>HEAD OFFICE</b><br>42 fernhill road<br>ashby, midshire, ab1 2cd.</p>
    <p style="margin-top:14px"><b>E-MAIL</b><br>info@nbr-example.com</p>
    <p style="margin-top:14px"><b>CONTACT</b><br>Landline: 111 5550 184<br>Fax: 111 5550 197</p>
  </div>
</div>

<footer class="footer" style="left:51px;top:1098px">Copyright © Northfield Bio Resins. All rights reserved<br>Terms of Service &nbsp;|&nbsp; Privacy Policy &nbsp;|&nbsp; About Us &nbsp;|&nbsp; Contact Us</footer>

<!-- ===== INNER PAGE 1 ===== -->
<div class="page-label" style="top:1209px">INNER PAGE 1</div>
<nav class="nav" style="left:432px;top:1313px">
  <span>Home</span><span class="sep">|</span><span class="active">Product Catalogue</span><span class="sep">|</span><span>About Us</span><span class="sep">|</span><span>Business Partners</span><span class="sep">|</span><span>Press Releases</span><span class="sep">|</span><span>Contact Us</span>
</nav>
<header class="abs banner-inner" style="top:1344px">
  <div class="brand-inner" style="top:48px"><span class="code">NBR</span>Northfield BioResins</div>
  <div class="tagline" style="left:548px;top:28px;width:500px;height:82px;font-size:44px;line-height:82px;padding-left:14px;background:linear-gradient(90deg,var(--green-pale) 75%,rgba(216,234,181,0))">Customers are "Partners"</div>
  <div class="art" role="img" aria-label="Green feather illustration" style="left:1062px;top:14px;width:80px;height:112px"></div>
</header>
<div class="crumb" style="top:1491px">Home &nbsp;- Product Catalogue</div>

<div class="abs" style="left:44px;top:1558px;width:630px">
  <h1 class="col-title">Products Catalogue</h1>
  <p style="margin-top:14px;line-height:22px">Northfield BioResins biodegradable plastic properties are comparable to conventional, petroleum-based, Polyethylene (PE) and Polypropylene (PP) plastics. Composition, biodegradability, and energy efficient processing represent a few differentiating characteristics from conventional plastics.</p>
  <p style="margin-top:20px;line-height:22px">Our biodegradable plastic is derived from poultry feathers (rather than petroleum), it biodegrades within months in landfill conditions, and it takes less energy to process. Unlike other marketed bioplastics, our bioplastic does not require inputs from the food chain, thereby stabilizing the cost of raw material inputs.</p>
  <p style="margin-top:20px">Consumer products manufactured with Northfield BioResins resin include:</p>
  <p style="margin-top:20px;font-weight:600;color:#555">1) Greenhouse &amp; Nursery Containers – 3"to 4" pots</p>
</div>

<div class="txt" style="left:44px;top:1913px;width:230px"><b>Green Houses:</b><br>Lorem Ipsum is simply<br>dummy text of the printing.</div>
<div class="thumb ph-green" role="img" aria-label="Greenhouse main photo" style="left:473px;top:1916px;width:211px;height:211px"></div>
<div class="thumb ph-green" role="img" aria-label="Greenhouse photo 1" style="left:62px;top:2034px;width:96px;height:93px"></div>
<div class="thumb ph-green" role="img" aria-label="Greenhouse photo 2" style="left:164px;top:2034px;width:96px;height:93px"></div>
<div class="thumb ph-green" role="img" aria-label="Greenhouse photo 3" style="left:267px;top:2034px;width:96px;height:93px"></div>
<div class="thumb ph-green" role="img" aria-label="Greenhouse photo 4" style="left:369px;top:2034px;width:96px;height:93px"></div>

<div class="txt" style="left:44px;top:2173px;width:230px"><b>Nursery Containers:</b><br>Lorem Ipsum is simply<br>dummy text of the printing.</div>
<div class="thumb ph-grey" role="img" aria-label="Nursery container main photo" style="left:473px;top:2178px;width:211px;height:209px"></div>
<div class="thumb ph-grey" role="img" aria-label="Nursery container photo 1" style="left:62px;top:2294px;width:96px;height:93px"></div>
<div class="thumb ph-grey" role="img" aria-label="Nursery container photo 2" style="left:164px;top:2294px;width:96px;height:93px"></div>
<div class="thumb ph-grey" role="img" aria-label="Nursery container photo 3" style="left:267px;top:2294px;width:96px;height:93px"></div>
<div class="thumb ph-grey" role="img" aria-label="Nursery container photo 4" style="left:369px;top:2294px;width:96px;height:93px"></div>

<div class="txt" style="left:44px;top:2452px;width:600px;font-weight:600;color:#555">2) Agricultural Films – plastic mulch used by vegetable growers<br>&nbsp;&nbsp;&nbsp;&nbsp;as ground cover</div>

<div class="txt" style="left:44px;top:2516px;width:230px"><b>Agricultural Films</b><br>Lorem Ipsum is simply<br>dummy text of the printing.</div>
<div class="thumb ph-film" role="img" aria-label="Agricultural film main photo" style="left:473px;top:2502px;width:211px;height:210px"><span class="num" style="bottom:auto;top:100px;font-size:17px">Main Image</span></div>
<div class="thumb ph-film" role="img" aria-label="Agricultural film photo 1" style="left:62px;top:2618px;width:96px;height:94px"><span class="num">1</span></div>
<div class="thumb ph-film" role="img" aria-label="Agricultural film photo 2" style="left:164px;top:2618px;width:96px;height:94px"><span class="num">2</span></div>
<div class="thumb ph-film" role="img" aria-label="Agricultural film photo 3" style="left:267px;top:2618px;width:96px;height:94px"><span class="num">3</span></div>
<div class="thumb ph-film" role="img" aria-label="Agricultural film photo 4" style="left:369px;top:2618px;width:96px;height:94px"><span class="num">4</span></div>

<div class="abs" style="left:44px;top:2772px;width:630px;line-height:22px">
  <p>Focusing on reducing vegetable farmer and greenhouse/nursery labor and disposal expenses, the biodegradable nature of the agricultural films will allow the plastic to be disked back into the field following planting season drastically reducing removal and disposal costs.</p>
  <p style="margin-top:20px">Similarly, pots and containers can be planted directly in the ground, reducing the amount of time spent repotting and eliminating fees associated with disposal.</p>
  <p style="margin-top:20px">In contrast to existing biodegradable plastics that are significantly more expensive, Northfield BioResins intends to keep its biodegradable plastic's market price competitive with conventional, petroleum-based alternatives. Low-demand, low-cost inputs and energy efficient production creates a cost structure that allows competitive market pricing.</p>
</div>

<div class="divider" style="left:736px;top:1555px;height:1550px"></div>

<div class="box" style="left:796px;top:1551px;width:357px;height:307px">
  <div class="box-head">Business Partners</div>
  <div class="box-body" style="color:var(--text)">
    <p style="font-weight:600;color:#555">Following are some business parners:</p>
    <ul class="list">
      <li>Lorum Ipsum Partner 1</li><li>Lorum Ipsum Partner 2</li><li>Lorum Ipsum Partner 3</li>
      <li>Lorum Ipsum Partner 4</li><li>Lorum Ipsum Partner 5</li><li>Lorum Ipsum Partner 6</li>
      <li>Lorum Ipsum Partner 7</li><li>Lorum Ipsum Partner 8</li><li>Lorum Ipsum Partner 9</li>
    </ul>
  </div>
</div>

<div class="box" style="left:796px;top:1940px;width:357px;height:224px">
  <div class="box-head">Contact Us</div>
  <div class="box-body" style="padding-top:14px">
    <p><b>HEAD OFFICE</b><br>42 fernhill road<br>ashby, midshire, ab1 2cd.</p>
    <p style="margin-top:14px"><b>E-MAIL</b><br>info@nbr-example.com</p>
    <p style="margin-top:14px"><b>CONTACT</b><br>Landline: 111 5550 184<br>Fax: 111 5550 197</p>
  </div>
</div>

<footer class="footer" style="left:44px;top:3092px">Copyright © Northfield Bio Resins. All rights reserved<br>Terms of Service &nbsp;|&nbsp; Privacy Policy &nbsp;|&nbsp; About Us &nbsp;|&nbsp; Contact Us</footer>

<!-- ===== INNER PAGE 2 ===== -->
<div class="page-label" style="top:3216px">INNER PAGE 2</div>
<nav class="nav" style="left:436px;top:3331px">
  <span>Home</span><span class="sep">|</span><span>Product Catalogue</span><span class="sep">|</span><span class="active">About Us</span><span class="sep">|</span><span>Business Partners</span><span class="sep">|</span><span>Press Releases</span><span class="sep">|</span><span>Contact Us</span>
</nav>
<header class="abs banner-inner" style="top:3362px">
  <div class="brand-inner" style="top:48px"><span class="code">NBR</span>Northfield BioResins</div>
  <div class="tagline" style="left:548px;top:28px;width:500px;height:82px;font-size:44px;line-height:82px;padding-left:14px;background:linear-gradient(90deg,var(--green-pale) 75%,rgba(216,234,181,0))">Customers are "Partners"</div>
  <div class="art" role="img" aria-label="Green feather illustration" style="left:1062px;top:14px;width:80px;height:112px"></div>
</header>
<div class="crumb" style="top:3509px">Home &nbsp;- About Us</div>

<div class="abs" style="left:47px;top:3576px;width:680px;line-height:20px">
  <h1 class="col-title">About Us</h1>
  <p style="margin-top:12px">Northfield BioResins is a green-technology start-up company implementing cutting edge technology and custom-designed machines to manufacture bioplastics derived from poultry feathers on an industrial scale for local, national and international agricultural, industrial and consumer markets.</p>
  <p style="margin-top:18px"><b style="color:#555">NBR vs. Conventional Plastics:</b><br>Northfield BioResins biodegradable plastics' cost to consumer and physical properties are comparable to conventional, petroleum-based, Polyethylene (PE) and Polypropylene (PP) plastics. (Which properties are similar???)<br>Composition, biodegradability, and energy efficient manufacturing represent the most significant differentiating characteristics from conventional plastics. Our biodegradable plastic is derived from poultry feathers, a 100% renewable biomass; it biodegrades within months in landfill conditions and requires less energy to process.</p>
  <p style="margin-top:18px"><b style="color:#555">NBR vs. Other Bioplastics</b><br>Unlike other marketed bioplastics, ours does not require inputs from the food chain. This stabilizes the cost of our raw material and keeps final cost to consumer competitive with petroleum based products. It also eliminates potential impact on the availability and cost of global food products, which is a risk inherent with bioplastics manufactured from corn, milk, ....</p>
  <p style="margin-top:18px"><b style="color:#555">Our Founder:</b><br>Marco Hallworth, president of Northfield BioResins brings a wealth of experience in agriculture, poultry, and business, is the entrepreneur behind the company's creation and development.</p>
  <p style="margin-top:18px"><b style="color:#555">Among Northfield BioResins' goals are:</b></p>
  <div class="bullets" style="margin-top:16px">
    <p>• Reducing petro-plastic waste</p>
    <p>• Reducing CO2 emissions from processing by 30%, or more, as compared to<br>&nbsp;&nbsp;petro-plastic alternatives</p>
    <p>• Reduce the life-cycle of carbon by re-fixing and generating "new" carbon as<br>&nbsp;&nbsp;quickly as ten to fifteen years to be used to generate new energy for future plant<br>&nbsp;&nbsp;growth</p>
    <p>• Add value to poultry feathers, an agricultural waste product</p>
    <p>• Boost biodiesel production by creating demand for glycerol (by-product of<br>&nbsp;&nbsp;biodiesel production, and an ingredient in our bioplastics)</p>
    <p>• Form relationships and carry out day-to-day business with honesty and integrity</p>
  </div>
</div>

<div class="box" style="left:796px;top:3569px;width:357px;height:545px">
  <div class="box-head">Proprietary Material</div>
  <div class="box-body" style="color:var(--text)">
    <p style="font-weight:600;color:#555;line-height:20px">Material Used in Manufacturing of our products are:</p>
    <ul class="list" style="margin-top:18px">
      <li>biodegradable</li><li>plastic</li><li>bioplastic</li><li>bioresin</li><li>feather</li>
      <li>flower pots</li><li>row cover</li><li>mulch</li><li>gardening</li><li>horticulture</li>
      <li>green/recycle/envirionmental</li><li>polymer</li><li>glycerol</li><li>biodiesel</li><li>green industry</li>
      <li>green business</li><li>eco friendly</li><li>carbon</li><li>carbon footprint</li>
    </ul>
  </div>
</div>

<div class="box" style="left:796px;top:4171px;width:357px;height:402px">
  <div class="box-head">Product Catalogue</div>
  <div class="box-body" style="color:var(--text);line-height:19px;padding-top:18px">
    <div class="cat-item"><b>Nursery Containers</b><br>Lorem Ipsum is simply<br>dummy text of the printing.<div class="ph ph-grey" role="img" aria-label="Nursery container thumbnail"></div></div>
    <div class="cat-item"><b>Green Houses</b><br>Lorem Ipsum is simply<br>dummy text of the printing.<div class="ph ph-green" role="img" aria-label="Greenhouse thumbnail"></div></div>
    <div class="cat-item" style="height:84px"><b>Agricultural Films</b><br>Lorem Ipsum is simply<br>dummy text of the printing.<div class="ph ph-film" role="img" aria-label="Agricultural film thumbnail"></div></div>
    <p style="font-weight:700;color:#555;text-decoration:underline">More</p>
  </div>
</div>

<footer class="footer" style="left:44px;top:4604px">Copyright © Northfield Bio Resins. All rights reserved<br>Terms of Service &nbsp;|&nbsp; Privacy Policy &nbsp;|&nbsp; About Us &nbsp;|&nbsp; Contact Us</footer>

</body>
</html>
```